Mailer Postcard for Potential Bankruptcy Clients

The postcard will be printed at 8.5"x6" to abide by the specification at the following link: https://www.mailtrelbo.com/submitting-art/specs/. I want an attractive two sided post card that includes my logo (see attachment). The design would have to have room for the website address, phone number, two location addresses and give them information about a civil action pending against them (You are being sued in X county (case# xxyx). We can help.). I don't really like the visuals of the attached postcard, so please use as a general guide for what I am trying to do. Ultimately, I want an ad that gets people to call me so I can help them.

I also want it to be compatible with the website (LoanHarbor.Legal).

Target Market(s)

Potential bankruptcy clients.

Industry/Entity Type

Legal

Colors

Designer to choose colors to be used in the design.

Requirements
Must have
• Phone number, addresses, website, and place for text regarding pending legal action against the receiver. Should say something to the effect: You have a pending legal action in (county name) County (court name [superior, magistrate, ect.]). Let us help you deal with it responsibly.
• Please note the design specifications at this link:

```html
<!DOCTYPE html>
<html lang="en">
<head>
<meta charset="utf-8">
<title>Loan Harbor Law Group – Mailer Postcard</title>
<link href="https://fonts.googleapis.com/css2?family=Raleway:ital,wght@0,400;0,500;0,600;0,700;0,800;1,500&family=Open+Sans:ital,wght@0,400;0,600;1,400;1,600&display=swap" rel="stylesheet">
<style>
  :root{
    --green:#6db46f;
    --green-dark:#4f9a52;
    --green-light:#8fc88f;
    --charcoal:#2f3030;
    --charcoal-2:#3a3b3b;
    --ink:#222;
    --grey-text:#444;
    --panel:#f1f1f1;
    --slot:#e3e3e3;
    --white:#fff;
    --page:#ececec;
  }
  *{box-sizing:border-box;margin:0;padding:0}
  html,body{width:902px;height:1200px;overflow:hidden}
  body{background:var(--page);position:relative;font-family:"Open Sans",sans-serif;color:var(--ink)}
  .card{position:absolute;width:782px;height:505px;background:var(--white);overflow:hidden;box-shadow:0 4px 14px rgba(0,0,0,.25)}
  .abs{position:absolute}

  /* ---------- FRONT ---------- */
  .front{left:50px;top:48px}
  .front .hero-bg{left:0;top:0;width:782px;height:300px;background:linear-gradient(90deg,#2c2d2d 0%,#3b3c3c 45%,#55595a 75%,#4a4d4e 100%)}
  .front .hero-photo{left:520px;top:0;width:262px;height:300px;background:radial-gradient(ellipse at 60% 45%,rgba(190,190,185,.35),rgba(70,72,72,0) 70%)}
  .front .band-white{left:0;top:300px;width:782px;height:22px;background:var(--white)}
  .front .band-dark{left:0;top:322px;width:782px;height:30px;background:var(--charcoal)}
  .front .footer-line{left:0;top:477px;width:782px;height:4px;background:var(--charcoal)}
  .front .footer-band{left:0;top:481px;width:782px;height:24px;background:var(--green)}
  .front .frame{left:36px;top:10px;width:224px;height:352px}
  .front .headline{left:377px;top:28px;font-family:"Raleway",sans-serif;font-weight:700;font-size:31px;line-height:38px;color:var(--white);letter-spacing:.2px}
  .front .headline .accent{color:var(--green-light)}
  .front .perks{left:378px;top:116px;list-style:none}
  .front .perks li{font-family:"Open Sans",sans-serif;font-style:italic;font-weight:600;font-size:12.5px;color:var(--white);height:20.2px;line-height:20px;padding-left:25px;position:relative}
  .front .perks li::before{content:"";position:absolute;left:0;top:5px;width:10px;height:10px;border-radius:50%;background:var(--green-light)}
  .front .cta{left:384px;top:312px;width:348px;height:98px;border-radius:4px;background:linear-gradient(180deg,var(--green) 0%,var(--green) 38%,#e9f3e9 60%,#b9dbb9 100%);box-shadow:0 3px 6px rgba(0,0,0,.3);text-align:center}
  .front .cta-label{font-family:"Raleway",sans-serif;font-weight:700;font-size:20px;color:var(--white);margin-top:9px}
  .front .cta-phone{display:flex;align-items:center;justify-content:center;gap:8px;margin-top:6px;font-family:"Raleway",sans-serif;font-weight:800;font-size:34px;color:var(--charcoal)}
  .front .brand{left:62px;top:396px}
  .front .brand-name{font-family:"Raleway",sans-serif;font-weight:600;font-size:26px;color:var(--charcoal-2);display:flex;align-items:center;gap:12px}
  .front .brand-name .dot{width:14px;height:14px;border-radius:50%;background:var(--green)}
  .front .brand-sub{font-family:"Raleway",sans-serif;font-size:11px;letter-spacing:2px;color:var(--grey-text);margin:2px 0 0 26px}
  .front .brand-by{font-family:"Open Sans",sans-serif;font-style:italic;font-size:9px;color:var(--green-dark);margin:2px 0 0 26px}
  .front .more{left:384px;top:432px;width:348px;text-align:center;font-family:"Raleway",sans-serif}
  .front .more p{font-weight:700;font-size:14px;color:var(--ink)}
  .front .more .web{font-weight:700;font-size:14px;letter-spacing:3px;margin-top:6px}

  /* ---------- BACK ---------- */
  .back{left:88px;top:622px}
  .back .stressed-photo{left:0;top:0;width:175px;height:158px;background:linear-gradient(135deg,#f4f4f4,#d8d8d8)}
  .back .notice{left:175px;top:0;width:223px;height:102px;background:var(--green);padding:16px 10px 0 10px;color:var(--white)}
  .back .notice h3{font-family:"Raleway",sans-serif;font-weight:500;font-size:10.5px;white-space:nowrap}
  .back .field{display:flex;align-items:center;margin-top:9px;font-family:"Open Sans",sans-serif;font-size:7.5px;font-weight:600}
  .back .field span{width:70px}
  .back .field i{display:block;width:134px;height:14px;background:var(--white)}
  .back .help{left:175px;top:102px;width:223px;height:56px;background:var(--panel);padding:8px 10px;font-family:"Raleway",sans-serif;font-weight:500;font-size:16.5px;line-height:21px;color:var(--charcoal-2)}
  .back .about{left:0;top:158px;width:398px;height:128px;background:var(--green-light);padding:8px 20px 0 20px}
  .back .about h2{font-family:"Raleway",sans-serif;font-weight:700;font-size:12px;color:var(--ink)}
  .back .about p{font-size:7.3px;line-height:9.8px;color:#1e2a1e;margin-top:3px;width:312px}
  .back .services{left:0;top:286px;width:398px;height:118px;background:var(--white);padding:8px 20px}
  .back .services h2{font-family:"Raleway",sans-serif;font-weight:600;font-size:12px;color:var(--green-dark)}
  .back .services .intro{font-family:"Raleway",sans-serif;font-weight:700;font-size:9.5px;line-height:12.5px;margin-top:3px;color:var(--ink);width:312px}
  .back .svc-cols{display:flex;gap:16px;margin-top:6px}
  .back .svc-cols ul{list-style:none;width:185px}
  .back .svc-cols li{font-style:italic;font-size:8.5px;line-height:15px;padding-left:12px;position:relative}
  .back .svc-cols li::before{content:"";position:absolute;left:0;top:5px;width:5px;height:5px;border-radius:50%;background:var(--green)}
  .back .divider{left:398px;top:0;width:24px;height:505px;background:var(--charcoal)}
  .back .locations{left:0;top:404px;width:398px;height:101px;background:var(--charcoal);padding:9px 20px 0;color:var(--white)}
  .back .locations h4{font-family:"Open Sans",sans-serif;font-weight:600;font-size:8.4px;line-height:12px;color:var(--green-light);white-space:nowrap}
  .back .addr-row{display:flex;margin-top:9px}
  .back .addr{display:flex;gap:7px;width:198px;font-size:7.8px;line-height:10px;font-weight:600}
  .back .contact-row{display:flex;align-items:center;margin-top:11px;height:24px}
  .back .contact{display:flex;align-items:center;gap:7px;width:198px;font-family:"Raleway",sans-serif;font-weight:800;line-height:24px}
  .back .contact.phone{font-size:19px}
  .back .contact.web{font-size:13px}
  .back .team-frame{left:340px;top:150px;width:160px;height:164px}
  .back .mail-side{left:422px;top:0;width:360px;height:505px;background:var(--white)}
  .back .return-brand{left:450px;top:28px;width:120px;text-align:center}
  .back .return-brand .name{font-family:"Raleway",sans-serif;font-weight:600;font-size:13px;color:var(--charcoal-2);display:flex;align-items:center;justify-content:center;gap:5px}
  .back .return-brand .name .dot{width:8px;height:8px;border-radius:50%;background:var(--green)}
  .back .return-brand .sub{font-family:"Raleway",sans-serif;font-size:6px;letter-spacing:1.5px;color:var(--grey-text);margin-top:2px}
  .back .return-brand .by{font-style:italic;font-size:5px;color:var(--green-dark)}
  .back .stamp{left:674px;top:26px;width:108px;height:102px;background:var(--slot)}
  .back .address-block{left:452px;top:318px;width:330px;height:172px;background:var(--slot)}
</style>
</head>
<body>

<section class="card front" aria-label="Postcard front">
  <div class="abs hero-bg"></div>
  <div class="abs hero-photo" role="img" aria-label="Faded photo of a relieved man in a shirt and tie stretching his arms"></div>
  <div class="abs band-white"></div>
  <div class="abs band-dark"></div>
  <div class="abs footer-line"></div>
  <div class="abs footer-band"></div>

  <svg class="abs frame" viewBox="0 0 224 352">
    <defs>
      <linearGradient id="handsFill" x1="0" y1="0" x2="1" y2="1">
        <stop offset="0" stop-color="#2a4a66"/>
        <stop offset=".5" stop-color="#1d2f44"/>
        <stop offset="1" stop-color="#2b3d52"/>
      </linearGradient>
    </defs>
    <rect x="3" y="3" width="218" height="346" rx="26" fill="var(--white)" stroke="var(--green)" stroke-width="5"/>
    <rect x="10" y="10" width="204" height="332" rx="20" fill="url(#handsFill)" role="img" aria-label="Photo of a businessman's hands cupped around a glowing dollar sign"/>
  </svg>

  <h1 class="abs headline">GET OUT OF DEBT AND<br><span class="accent">RESTORE YOUR CREDIT</span></h1>
  <ul class="abs perks">
    <li>Free Credit Education Program</li>
    <li>$0 Down Bankruptcy Options</li>
    <li>Stop Collection Calls</li>
    <li>Stop Foreclosures &amp; Repossessions</li>
    <li>Stop Garnishments</li>
    <li>Fix Credit Report Errors</li>
    <li>Prosecute Illegal Debt Collection Practices</li>
    <li>Prosecute Post Discharge Violations</li>
    <li>Student Loan Representation</li>
  </ul>

  <div class="abs cta">
    <div class="cta-label">Schedule Appointment</div>
    <div class="cta-phone">
      <svg width="28" height="28" viewBox="0 0 28 28" aria-hidden="true">
        <circle cx="14" cy="14" r="12" fill="none" stroke="var(--charcoal)" stroke-width="2.2"/>
        <path d="M10 8.5c.6-.5 1.4-.4 1.8.2l1.2 2c.3.6.2 1.2-.3 1.6l-.8.6c.6 1.5 1.6 2.6 3 3.3l.7-.8c.4-.5 1.1-.6 1.6-.3l2 1.2c.6.4.8 1.2.3 1.8l-.9 1.1c-.6.7-1.6.9-2.4.6-3.6-1.5-6-4-7.3-7.6-.3-.9 0-1.8.6-2.4z" fill="var(--charcoal)"/>
      </svg>
      <span>(404) 555-0187</span>
    </div>
  </div>

  <div class="abs brand">
    <div class="brand-name"><span class="dot"></span>Loan Harbor</div>
    <div class="brand-sub">LAW GROUP</div>
    <div class="brand-by">by Attorney M. Velasco</div>
  </div>

  <div class="abs more">
    <p>For more information visit us:</p>
    <p class="web">www.loanharbor.legal</p>
  </div>
</section>

<section class="card back" aria-label="Postcard back">
  <div class="abs stressed-photo" role="img" aria-label="Photo of a stressed man covering his eyes, surrounded by words like debt, loss, pain and stress"></div>

  <div class="abs notice">
    <h3>YOU HAVE A PENDING LEGAL ACTION IN</h3>
    <div class="field"><span>COUNTY NAME :</span><i></i></div>
    <div class="field"><span>COURT NAME :</span><i></i></div>
  </div>
  <div class="abs help">LET US HELP YOU DEAL<br>WITH IT RESPONSIBLY</div>

  <div class="abs about">
    <h2>WHO ARE WE?</h2>
    <p>We are a Georgia Law Firm that is dedicated to being a one-stop shop for all debt woes that Georgians face. We are experienced bankruptcy attorneys that understand that people need more than just a bankruptcy lawyer. People need someone that is experienced in handling all of the practical aspects of avoiding bankruptcy, recovering from bankruptcy quickly, tackling stubborn student loans, and punishing abusive debt collectors when they violate the law. If you came to this website and have read this far, you should contact us to see if we can help you.</p>
  </div>

  <div class="abs services">
    <h2>OUR SERVICES</h2>
    <p class="intro">Below are a few services that we offer. Contact us to get more details and see what we can do for you.</p>
    <div class="svc-cols">
      <ul>
        <li>Mortgage Loan Modifications</li>
        <li>Credit Report Inaccuracies &amp; Errors</li>
        <li>Student Loans</li>
      </ul>
      <ul>
        <li>Debt Collection Violations</li>
        <li>Bankruptcy</li>
        <li>Free Credit Rebuilding Program</li>
      </ul>
    </div>
  </div>

  <div class="abs locations">
    <h4>We're located in the heart of downtown Atlanta, GA, and historic Douglasville, GA at:</h4>
    <div class="addr-row">
      <div class="addr">
        <svg width="8" height="11" viewBox="0 0 8 11" aria-hidden="true"><path d="M4 0a4 4 0 0 1 4 4c0 3-4 7-4 7S0 7 0 4a4 4 0 0 1 4-4z" fill="var(--green-light)"/><circle cx="4" cy="4" r="1.5" fill="var(--charcoal)"/></svg>
        <span>418 Larkmoor Ave., NW Suite #1400<br>Atlanta, Georgia 30303</span>
      </div>
      <div class="addr">
        <svg width="8" height="11" viewBox="0 0 8 11" aria-hidden="true"><path d="M4 0a4 4 0 0 1 4 4c0 3-4 7-4 7S0 7 0 4a4 4 0 0 1 4-4z" fill="var(--green-light)"/><circle cx="4" cy="4" r="1.5" fill="var(--charcoal)"/></svg>
        <span>5120 W. Fenwick St. Douglasville,<br>Georgia 30134</span>
      </div>
    </div>
    <div class="contact-row">
      <div class="contact phone">
        <svg width="16" height="16" viewBox="0 0 28 28" aria-hidden="true">
          <circle cx="14" cy="14" r="12" fill="none" stroke="var(--white)" stroke-width="2.4"/>
          <path d="M10 8.5c.6-.5 1.4-.4 1.8.2l1.2 2c.3.6.2 1.2-.3 1.6l-.8.6c.6 1.5 1.6 2.6 3 3.3l.7-.8c.4-.5 1.1-.6 1.6-.3l2 1.2c.6.4.8 1.2.3 1.8l-.9 1.1c-.6.7-1.6.9-2.4.6-3.6-1.5-6-4-7.3-7.6-.3-.9 0-1.8.6-2.4z" fill="var(--white)"/>
        </svg>
        <span>(404) 555-0187</span>
      </div>
      <div class="contact web">
        <svg width="12" height="12" viewBox="0 0 12 12" aria-hidden="true"><circle cx="6" cy="6" r="5" fill="none" stroke="var(--white)" stroke-width="1"/><ellipse cx="6" cy="6" rx="2.2" ry="5" fill="none" stroke="var(--white)" stroke-width="1"/><line x1="1" y1="6" x2="11" y2="6" stroke="var(--white)" stroke-width="1"/></svg>
        <span>www.loanharbor.legal</span>
      </div>
    </div>
  </div>

  <div class="abs divider"></div>
  <div class="abs mail-side"></div>

  <svg class="abs team-frame" viewBox="0 0 160 164">
    <defs>
      <linearGradient id="teamFill" x1="0" y1="0" x2="1" y2="1">
        <stop offset="0" stop-color="#e8eef3"/>
        <stop offset=".55" stop-color="#b9c9d6"/>
        <stop offset="1" stop-color="#dfe4e8"/>
      </linearGradient>
    </defs>
    <rect x="3" y="3" width="154" height="158" rx="22" fill="var(--white)" stroke="#cfcfcf" stroke-width="2"/>
    <rect x="12" y="12" width="136" height="140" rx="16" fill="url(#teamFill)" role="img" aria-label="Photo of a smiling couple shaking hands with an attorney across a desk"/>
  </svg>

  <div class="abs return-brand">
    <div class="name"><span class="dot"></span>Loan Harbor</div>
    <div class="sub">LAW GROUP</div>
    <div class="by">by Attorney M. Velasco</div>
  </div>
  <div class="abs stamp" aria-label="Postage area"></div>
  <div class="abs address-block" aria-label="Mailing address area"></div>
</section>

</body>
</html>
```